International tradind company needs a professional Business Card

We are an international trading company and we need a business card for our CEO and employers so they can give it away in their meetings and while networking.
We want the card design quality to cause an immediate "wow" and we count on you to do that!

key-words and concepts to communicate: trustworthiness, ethics, sucess, modern, global business, networking

Our favorite colours are blue and grey but we are open to suggestions.

It would be recommended that our logo was part of the card. You can see it in www.velmarholding.com . We also would like the following info on the card:
Name
position in the company
cell phone and personal email

```html
<!DOCTYPE html>
<html lang="en">
<head>
<meta charset="utf-8">
<title>Velmar Holding – Business Card</title>
<link href="https://fonts.googleapis.com/css2?family=Carlito:wght@400;700&display=swap" rel="stylesheet">
<style>
  :root {
    --page-bg: #eceeee;
    --card-white: #ffffff;
    --card-grey: #c9cacc;
    --brand-navy: #2a2470;
    --brand-sky: #5a8fd0;
    --band-top: #2a9bcc;
    --band-mid: #1d6aa6;
    --band-bottom: #1d3f82;
    --silver-light: #f2f2f2;
    --silver-dark: #8c8e92;
    --ink: #2b2b2b;
    --on-band: #ffffff;
  }
  html, body {
    margin: 0;
    padding: 0;
    width: 1129px;
    height: 1200px;
    overflow: hidden;
    background: var(--page-bg);
    font-family: "Carlito", "Calibri", sans-serif;
  }
  .card {
    position: absolute;
    width: 786px;
    height: 456px;
    box-shadow: 0 8px 18px rgba(0, 0, 0, 0.22);
    overflow: hidden;
  }
  .card--front { left: 166px; top: 89px; }
  .card--back  { left: 175px; top: 629px; }
  .card__art {
    position: absolute;
    inset: 0;
    width: 100%;
    height: 100%;
  }
  .brand-mark {
    position: absolute;
    left: 112px;
    top: 86px;
    width: 150px;
    height: 150px;
    border-radius: 50%;
    background: var(--brand-navy);
  }
  .brand-name {
    position: absolute;
    left: 318px;
    top: 106px;
    margin: 0;
    font-size: 64px;
    font-weight: 400;
    line-height: 1;
    color: var(--brand-navy);
  }
  .brand-tagline {
    position: absolute;
    left: 326px;
    top: 182px;
    margin: 0;
    font-size: 34px;
    line-height: 1;
    color: var(--brand-sky);
  }
  .website {
    position: absolute;
    left: 0;
    right: 0;
    top: 373px;
    margin: 0;
    text-align: center;
    font-size: 29px;
    font-weight: 700;
    color: var(--on-band);
  }
  .person__name {
    position: absolute;
    left: 176px;
    top: 100px;
    margin: 0;
    font-size: 28px;
    font-weight: 700;
    color: var(--ink);
  }
  .person__role {
    position: absolute;
    left: 176px;
    top: 140px;
    margin: 0;
    font-size: 24px;
    color: var(--ink);
  }
  .contacts {
    position: absolute;
    left: 172px;
    top: 262px;
    margin: 0;
    padding: 0;
    list-style: none;
    color: var(--on-band);
    font-size: 25px;
  }
  .contacts__item {
    display: flex;
    align-items: center;
    height: 40.5px;
  }
  .contacts__icon {
    width: 22px;
    height: 22px;
    margin-right: 17px;
    fill: none;
    stroke: var(--on-band);
    stroke-width: 1.8;
  }
</style>
</head>
<body>

<section class="card card--front" aria-label="Business card front">
  <svg class="card__art" viewBox="0 0 786 456" preserveAspectRatio="none" aria-hidden="true">
    <defs>
      <linearGradient id="front-face" x1="0" x2="1" y1="0" y2="0">
        <stop offset="0" stop-color="#dedfe0"/>
        <stop offset="0.25" stop-color="#ffffff"/>
        <stop offset="0.7" stop-color="#ffffff"/>
        <stop offset="1" stop-color="#c3c4c6"/>
      </linearGradient>
      <linearGradient id="front-band" x1="0" x2="0" y1="0" y2="1">
        <stop offset="0" stop-color="var(--band-top)"/>
        <stop offset="0.45" stop-color="var(--band-mid)"/>
        <stop offset="1" stop-color="var(--band-bottom)"/>
      </linearGradient>
      <linearGradient id="front-silver" x1="0" x2="1" y1="0" y2="0">
        <stop offset="0" stop-color="var(--silver-dark)"/>
        <stop offset="0.5" stop-color="var(--silver-light)"/>
        <stop offset="1" stop-color="var(--silver-dark)"/>
      </linearGradient>
    </defs>
    <rect width="786" height="456" fill="url(#front-face)"/>
    <path d="M0 311 Q393 268 786 317 L786 328 Q393 284 0 322 Z" fill="url(#front-silver)"/>
    <path d="M0 322 Q393 284 786 328 L786 456 L0 456 Z" fill="url(#front-band)"/>
  </svg>
  <span class="brand-mark" aria-hidden="true"></span>
  <h1 class="brand-name">Velmar Holding</h1>
  <p class="brand-tagline">Business Services</p>
  <p class="website">www.velmarholding.com</p>
</section>

<section class="card card--back" aria-label="Business card back">
  <svg class="card__art" viewBox="0 0 786 456" preserveAspectRatio="none" aria-hidden="true">
    <defs>
      <linearGradient id="back-face" x1="0" x2="1" y1="0" y2="0">
        <stop offset="0" stop-color="#c9cacc"/>
        <stop offset="0.3" stop-color="#ffffff"/>
        <stop offset="0.75" stop-color="#ffffff"/>
        <stop offset="1" stop-color="#d0d1d3"/>
      </linearGradient>
      <linearGradient id="back-band" x1="0" x2="0" y1="0" y2="1">
        <stop offset="0" stop-color="var(--band-top)"/>
        <stop offset="0.45" stop-color="var(--band-mid)"/>
        <stop offset="1" stop-color="var(--band-bottom)"/>
      </linearGradient>
      <linearGradient id="back-silver" x1="0" x2="1" y1="0" y2="0">
        <stop offset="0" stop-color="var(--silver-dark)"/>
        <stop offset="0.5" stop-color="var(--silver-light)"/>
        <stop offset="1" stop-color="var(--silver-dark)"/>
      </linearGradient>
    </defs>
    <rect width="786" height="456" fill="url(#back-face)"/>
    <path d="M0 240 Q393 212 786 246 L786 257 Q393 226 0 251 Z" fill="url(#back-silver)"/>
    <path d="M0 251 Q393 226 786 257 L786 456 L0 456 Z" fill="url(#back-band)"/>
  </svg>
  <h2 class="person__name">Name Surname</h2>
  <p class="person__role">Position</p>
  <ul class="contacts">
    <li class="contacts__item">
      <svg class="contacts__icon" viewBox="0 0 24 24" aria-hidden="true"><path d="M6 3 L9 3 L10 8 L8 9.5 Q10 15 14.5 16 L16 14 L21 15 L21 18 Q20 21 17 21 Q6 19 3 7 Q3 4 6 3 Z"/></svg>
      <span>+351210457320</span>
    </li>
    <li class="contacts__item">
      <svg class="contacts__icon" viewBox="0 0 24 24" aria-hidden="true"><rect x="5" y="2" width="14" height="20" rx="2"/><line x1="10" y1="18.5" x2="14" y2="18.5"/></svg>
      <span>+351912604278</span>
    </li>
    <li class="contacts__item">
      <svg class="contacts__icon" viewBox="0 0 24 24" aria-hidden="true"><rect x="2" y="5" width="20" height="14"/><path d="M2 5 L12 13 L22 5"/></svg>
      <span>contact@velmarholding.com</span>
    </li>
    <li class="contacts__item">
      <svg class="contacts__icon" viewBox="0 0 24 24" aria-hidden="true"><path d="M2 10 L12 4 L22 10 Z"/><rect x="4" y="10" width="16" height="10"/><rect x="10" y="13" width="4" height="7"/></svg>
      <span>PORTUGAL, Rua das Amoreiras, 12, 2o Esq</span>
    </li>
  </ul>
</section>

</body>
</html>
```